Business Cards for wirefen.com.au
Logo already designed by Quillnoxa
Professional
Liam Forbury
Technical Engineer
Mobile: 0437 125 806
liam@wirefen.com.au
www.wirefen.com.au
Should have the text: "Cloud Application Development"

```html
<!DOCTYPE html>
<html lang="en">
<head>
<meta charset="utf-8">
<title>wirefen.com.au Stationery</title>
<link href="https://fonts.googleapis.com/css2?family=Nunito:wght@700&family=Open+Sans:wght@400;600&display=swap" rel="stylesheet">
<style>
  :root {
    --page: #ffffff;
    --paper: #ffffff;
    --ink: #3b3d40;
    --ink-soft: #6d7075;
    --blue-deep: #0b4f9c;
    --blue: #1f7fd6;
    --blue-light: #4fb0f0;
    --grey-band: #5b5e62;
    --shadow: rgba(0, 0, 0, 0.28);
  }
  * { margin: 0; padding: 0; box-sizing: border-box; }
  html, body { width: 1200px; height: 681px; overflow: hidden; background: var(--page); }
  body { position: relative; font-family: "Open Sans", Arial, sans-serif; color: var(--ink); }

  .sheet {
    position: absolute;
    background: var(--paper);
    box-shadow: 3px 4px 7px var(--shadow);
    overflow: hidden;
  }

  .footer-bands { position: absolute; left: 0; right: 0; bottom: 0; }
  .footer-bands .grey-rule { background: var(--grey-band); }
  .footer-bands .blue-band {
    background: linear-gradient(90deg, var(--blue-deep) 0%, var(--blue) 55%, var(--blue-deep) 100%);
  }

  .brand-name {
    font-family: "Nunito", Arial, sans-serif;
    font-weight: 700;
    color: var(--ink);
    letter-spacing: 0.2px;
    position: absolute;
    white-space: nowrap;
  }

  /* Envelope front */
  .envelope-front { left: 60px; top: 91px; width: 504px; height: 233px; }
  .envelope-front .brand-name { left: 14px; top: 10px; font-size: 27px; }
  .envelope-front .grey-rule { height: 8px; margin-bottom: 5px; }
  .envelope-front .blue-band { height: 34px; }

  /* Envelope back */
  .envelope-back { left: 60px; top: 372px; width: 504px; height: 240px; }
  .envelope-back .flap { position: absolute; left: 0; top: 0; width: 100%; height: 100%; }
  .envelope-back .brand-name {
    left: 0; right: 0; top: 96px; text-align: center; font-size: 18px; color: var(--blue);
  }

  /* Letterhead */
  .letterhead { left: 619px; top: 43px; width: 384px; height: 588px; }
  .letterhead .brand-name { left: 22px; top: 18px; font-size: 24px; }
  .letterhead .contact-line {
    position: absolute; left: 24px; top: 55px; font-size: 6.5px; color: var(--ink-soft);
  }
  .letterhead .grey-rule { height: 7px; margin-bottom: 4px; }
  .letterhead .blue-band { height: 30px; }

  /* Business card front */
  .card-front { left: 970px; top: 259px; width: 201px; height: 120px; }
  .card-front .top-strip {
    position: absolute; right: 0; top: 0; width: 60px; height: 100%;
    background: linear-gradient(180deg, var(--blue-light), var(--blue));
    opacity: 0.18;
  }
  .card-front .person { position: absolute; left: 12px; top: 12px; }
  .card-front .person-name { font-size: 8px; font-weight: 600; color: var(--blue-deep); }
  .card-front .person-role { font-size: 6px; color: var(--ink-soft); }
  .card-front .details { position: absolute; left: 12px; top: 48px; font-size: 5.5px; line-height: 1.45; color: var(--ink-soft); }
  .card-front .brand-name { right: 10px; top: 82px; font-size: 14px; }
  .card-front .tagline { position: absolute; right: 10px; top: 101px; font-size: 5.5px; color: var(--ink-soft); }

  /* Business card back */
  .card-back {
    left: 970px; top: 403px; width: 201px; height: 120px;
    background: radial-gradient(ellipse at 50% 45%, var(--blue-light) 0%, var(--blue) 45%, var(--blue-deep) 100%);
  }
  .card-back .brand-name {
    left: 0; right: 0; top: 50px; text-align: center; font-size: 15px; color: #ffffff;
  }
</style>
</head>
<body>

  <section class="sheet envelope-front" aria-label="Envelope front">
    <div class="brand-name">wirefen.com.au</div>
    <div class="footer-bands">
      <div class="grey-rule"></div>
      <div class="blue-band"></div>
    </div>
  </section>

  <section class="sheet envelope-back" aria-label="Envelope back">
    <svg class="flap" viewBox="0 0 504 240" preserveAspectRatio="none" aria-hidden="true">
      <path d="M8 10 Q14 14 18 22 L238 70 Q252 74 266 70 L486 22 Q490 14 496 10" fill="none" stroke="#9a9da1" stroke-width="1"/>
      <path d="M0 6 L504 6" stroke="#c8cacd" stroke-width="1"/>
    </svg>
    <div class="brand-name">wirefen.com.au</div>
  </section>

  <section class="sheet letterhead" aria-label="Letterhead">
    <div class="brand-name">wirefen.com.au</div>
    <p class="contact-line">Email: liam@wirefen.com.au &nbsp;|&nbsp; www.wirefen.com.au</p>
    <div class="footer-bands">
      <div class="grey-rule"></div>
      <div class="blue-band"></div>
    </div>
  </section>

  <section class="sheet card-front" aria-label="Business card front">
    <div class="top-strip" aria-hidden="true"></div>
    <div class="person">
      <p class="person-name">Liam Forbury</p>
      <p class="person-role">Technical Engineer</p>
    </div>
    <div class="details">
      <p>Mobile: 0437 125 806</p>
      <p>liam@wirefen.com.au</p>
      <p>www.wirefen.com.au</p>
    </div>
    <div class="brand-name">wirefen.com.au</div>
    <p class="tagline">Cloud Application Development</p>
  </section>

  <section class="sheet card-back" aria-label="Business card back">
    <div class="brand-name">wirefen.com.au</div>
  </section>

</body>
</html>
```